Business Card Design

About Us
VaultNetix is a young and innovative company focusing on security and hosting solutions for global enterprise. To supply the high-performance, highly interconnected and low latency DDoS protection service, we distributed a large number of huge scrubbing centers all over the world. So VaultNetix is the first choice for enterprise to protect their network security.

Task detail
1. We hope that the business card can be filled with creativity, simple and technologe, the business card background is white, the business card text color and other colors are black, blue, green or your needs.

2. We need the source files provided by the successful bidder, such as *.psd, *.ai, etc.

3. One side contains the following:
-Logo
-Brin Sales Manager
-VAULTNETIX TECHNOLOGY CO., LIMITED
-Add:
9/F., Harmon Tower,
218 Pellow Street, Tai Hang, Kowloon,
HK
-Tel: 86-755-4172 0583
-Phone: 86-189 6041 3725
-Email: brin@vault-netix.com
-Web: www.vault-netix.com

4. The other side contains the following:
-Logo

5. Please find the attachment contains the logo PSD source files.

```html
<!DOCTYPE html>
<html lang="en">
<head>
<meta charset="utf-8">
<title>VaultNetix Business Card</title>
<link rel="stylesheet" href="https://fonts.googleapis.com/css2?family=Exo+2:wght@300;400;600&display=swap">
<style>
  :root {
    --stage: #e9ecee;
    --card-white: #ffffff;
    --card-shade: #f1f2f3;
    --teal: #2fb0c9;
    --lime: #7cc52a;
    --ink: #2f3033;
    --on-teal: #ffffff;
  }
  * { margin: 0; padding: 0; box-sizing: border-box; }
  html, body {
    width: 1200px; height: 901px; overflow: hidden;
    background: var(--stage);
    font-family: "Exo 2", "Segoe UI", sans-serif;
  }
  .card {
    position: absolute; left: 100px; top: 165px;
    width: 1000px; height: 572px;
    border-radius: 56px; overflow: hidden;
    background: linear-gradient(160deg, var(--card-white) 40%, var(--card-shade));
    box-shadow: 0 14px 36px rgba(0,0,0,.18);
  }
  .card__art { position: absolute; inset: 0; }
  .brand {
    position: absolute; left: 92px; top: 212px;
    display: flex; align-items: center; gap: 16px;
  }
  .brand__square { width: 44px; height: 44px; background: var(--ink); }
  .brand__name {
    font-weight: 600; font-size: 64px; letter-spacing: -1px;
    color: var(--ink); line-height: 1;
  }
  .details {
    position: absolute; right: 60px; top: 78px;
    text-align: right; color: var(--on-teal);
  }
  .person__name { font-size: 30px; font-weight: 400; letter-spacing: 2px; }
  .person__role { font-size: 22px; font-weight: 300; margin-top: 4px; }
  .address { margin-top: 80px; font-size: 23px; font-weight: 300; line-height: 1.3; }
  .contacts { list-style: none; margin-top: 62px; font-size: 20px; font-weight: 300; }
  .contacts li {
    display: flex; justify-content: flex-end; align-items: center;
    gap: 12px; height: 30px;
  }
  .contacts svg { width: 20px; height: 20px; fill: none; stroke: var(--on-teal); stroke-width: 1.8; }
</style>
</head>
<body>
  <div class="card">
    <svg class="card__art" viewBox="0 0 1000 572" preserveAspectRatio="none" aria-hidden="true">
      <path fill="var(--teal)" d="M575,0 C600,120 560,220 505,290 C450,360 420,450 420,572 L1000,572 L1000,0 Z"/>
      <path fill="var(--lime)" d="M560,0 C580,110 545,190 470,265 C520,200 550,120 545,0 Z"/>
      <path fill="var(--lime)" d="M468,318 C420,380 400,460 402,572 L416,572 C414,470 430,390 468,318 Z"/>
    </svg>

    <div class="brand">
      <span class="brand__square"></span>
      <span class="brand__name">VaultNetix</span>
    </div>

    <div class="details">
      <div class="person__name">JOHN BRINWELL</div>
      <div class="person__role">Managing Director</div>
      <div class="address">041.9th floor.Tower<br>Pellow Road THK</div>
      <ul class="contacts">
        <li>012 555 0148
          <svg viewBox="0 0 24 24"><path d="M5 3h4l2 5-3 2a12 12 0 0 0 6 6l2-3 5 2v4a2 2 0 0 1-2 2A18 18 0 0 1 3 5a2 2 0 0 1 2-2z"/></svg>
        </li>
        <li>012 555 0162
          <svg viewBox="0 0 24 24"><rect x="7" y="2" width="10" height="20" rx="2"/><line x1="11" y1="18" x2="13" y2="18"/></svg>
        </li>
        <li>012 555 0177
          <svg viewBox="0 0 24 24"><rect x="4" y="9" width="16" height="12" rx="1"/><path d="M7 9V3h10v6"/><line x1="8" y1="14" x2="16" y2="14"/><line x1="8" y1="17" x2="16" y2="17"/></svg>
        </li>
        <li>brin@vault-netix.com
          <svg viewBox="0 0 24 24"><rect x="3" y="5" width="18" height="14" rx="1"/><path d="M3 6l9 7 9-7"/></svg>
        </li>
        <li>www.vault-netix.com
          <svg viewBox="0 0 24 24"><circle cx="12" cy="12" r="9"/><path d="M3 12h18M12 3c3 3 3 15 0 18M12 3c-3 3-3 15 0 18"/></svg>
        </li>
      </ul>
    </div>
  </div>
</body>
</html>
```